Business card design for a world class martial arts and group fitness facility

We need a professional and eye catching design for a business card. The card will be used in networking as well as marketing.
We are a martial arts facility offering Taekwondo, Brazilian Jiu Jitsu, and group fitness. All of our programs are geared for kids and adults.
Our Taekwondo program is lead by a Hall of Fame instructor who was Instructor of the Year in 2015.
Our Brazilian Jiu Jitsu program is lead by a wold class instructor who is also a part of the renown Brazilian KLO team.
We offer 3 focused group fitness programs: Ridge kickboxing, Tandem Fitness, and The Quarry which are all lead by certified instructors in a small group setting.
Our facility is state of the art and has been recognized as such in nationally published magazines.
Our business is named The Forge which is the linear logo that is attached. This is the main logo. I also attached a circular logo we have used in some marketing material. Our Jiu Jitsu program is the KLO team logo. The Taekwondo program is the VORTEN Prime. It would be nice to somehow incorporate all 3 logos, but The Forge is most important.
We would like to use all 3 logos if possible but The Forge is the most important. We would like to have a place for a staff member's name while keeping the focus on the programs we offer.

```html
<!DOCTYPE html>
<html lang="en">
<head>
<meta charset="utf-8">
<title>The Forge – Business Card</title>
<link href="https://fonts.googleapis.com/css2?family=Open+Sans:wght@400;600;700&display=swap" rel="stylesheet">
<style>
  :root {
    --backdrop: #776767;
    --card: #3b3a3b;
    --card-edge: #2a292a;
    --light: #e4e4e4;
    --ink: #2b2b2b;
    --text: #f0f0f0;
    --garment: #444344;
    --tick: #f2f2f2;
    --accent: #b12a2a;
  }
  html, body {
    margin: 0;
    width: 1200px;
    height: 857px;
    overflow: hidden;
    background: var(--backdrop);
    font-family: "Open Sans", Arial, sans-serif;
  }
  .stage {
    position: relative;
    width: 1200px;
    height: 857px;
    display: flex;
    align-items: center;
    justify-content: center;
    gap: 40px;
  }
  .card {
    position: relative;
    width: 560px;
    height: 320px;
    background: var(--card);
    overflow: hidden;
    box-shadow: 0 2px 0 var(--card-edge);
  }
  .brand-disc {
    position: absolute;
    width: 250px;
    height: 250px;
    border-radius: 50%;
    background: var(--light);
    display: flex;
    align-items: center;
    justify-content: center;
    box-sizing: border-box;
    padding: 0 36px;
  }
  .brand-name {
    color: var(--ink);
    font-weight: 700;
    font-size: 30px;
    line-height: 1;
    letter-spacing: 1px;
    text-transform: uppercase;
    white-space: nowrap;
  }

  /* front */
  .front .brand-disc { left: 300px; top: 35px; }
  .name-plate {
    position: absolute;
    left: 0; top: 48px;
    width: 196px; height: 48px;
    background: var(--light);
    color: var(--ink);
    font-weight: 600;
    font-size: 19px;
    line-height: 48px;
    padding-left: 20px;
    box-sizing: border-box;
  }
  .garment {
    position: absolute;
    left: 110px; top: 215px;
    width: 140px; height: 110px;
    background: var(--garment);
    border-radius: 40px 40px 0 0;
  }
  .offer-title {
    position: absolute;
    left: 28px; top: 150px;
    margin: 0;
    color: var(--text);
    font-weight: 400;
    font-size: 32px;
    line-height: 40px;
  }
  .programs {
    position: absolute;
    right: 325px; top: 196px;
    margin: 0; padding: 0;
    list-style: none;
    color: var(--text);
  }
  .program {
    font-size: 14px;
    line-height: 24px;
    display: flex;
    justify-content: flex-end;
    align-items: center;
    gap: 5px;
  }
  .program svg { width: 15px; height: 15px; flex: none; }
  .sub-programs {
    margin: 0; padding: 0;
    list-style: none;
  }
  .sub-program {
    font-size: 10px;
    line-height: 15px;
    display: flex;
    justify-content: flex-end;
    align-items: center;
    gap: 4px;
  }
  .sub-program::before { content: "+"; font-weight: 700; }

  /* back */
  .back .brand-disc { left: 30px; top: 35px; }
  .partner {
    position: absolute;
    display: flex;
    align-items: center;
    gap: 10px;
    color: var(--text);
    font-weight: 700;
    font-size: 18px;
    text-transform: uppercase;
    white-space: nowrap;
  }
  .partner-square { width: 40px; height: 40px; background: var(--accent); flex: none; }
  .partner-circle { width: 40px; height: 40px; border-radius: 50%; background: #1c1c1c; border: 3px solid var(--accent); box-sizing: border-box; flex: none; }
  .partner.tkd { left: 330px; top: 90px; }
  .partner.bjj { left: 330px; top: 180px; }
</style>
</head>
<body>
<main class="stage">
  <section class="card back" aria-label="Card back">
    <div class="brand-disc"><span class="brand-name">The Forge</span></div>
    <div class="partner tkd"><span class="partner-square"></span>VORTEN Prime</div>
    <div class="partner bjj"><span class="partner-circle"></span>KLO</div>
  </section>

  <section class="card front" aria-label="Card front">
    <div class="garment" role="img" aria-label="Faint martial arts uniform illustration"></div>
    <div class="name-plate">Your Name Here</div>
    <h2 class="offer-title">we offering</h2>
    <ul class="programs">
      <li class="program">taekwondo <svg viewBox="0 0 16 16"><rect x="1" y="1" width="14" height="14" fill="none" stroke="var(--tick)" stroke-width="1.5"/><path d="M4 8l3 3 6-8" fill="none" stroke="var(--tick)" stroke-width="2"/></svg></li>
      <li class="program">brazilian Jiu Jitsu <svg viewBox="0 0 16 16"><rect x="1" y="1" width="14" height="14" fill="none" stroke="var(--tick)" stroke-width="1.5"/><path d="M4 8l3 3 6-8" fill="none" stroke="var(--tick)" stroke-width="2"/></svg></li>
      <li class="program">group fitness <svg viewBox="0 0 16 16"><rect x="1" y="1" width="14" height="14" fill="none" stroke="var(--tick)" stroke-width="1.5"/><path d="M4 8l3 3 6-8" fill="none" stroke="var(--tick)" stroke-width="2"/></svg></li>
      <li>
        <ul class="sub-programs">
          <li class="sub-program">Ridge kickboxing</li>
          <li class="sub-program">Tandem Fitness</li>
          <li class="sub-program">The Quarry</li>
        </ul>
      </li>
    </ul>
    <div class="brand-disc"><span class="brand-name">The Forge</span></div>
  </section>
</main>
</body>
</html>
```